Barrowdale Power Loft Chronic Pain Flyer

Double sided DL flyer required to promote a strength training studio to sufferers of chronic pain. Flyer will be displayed in osteopathy, chiropractic and massage clinics. Flyer should be clean, professional and appeal to an older (40+) demographic.

Target Market(s)

Chronic pain sufferers. Age 40+

Industry/Entity Type

Health And Wellness

Colors

Designer to choose colors to be used in the design.

Requirements
Must have
• See attached files for text copy and logo. Image(s) of people strength training with a coach or personal trainer, as well as images depicting pain in common parts of the body (such as those pictured in the supplied mock up)
• website address: barrowdalepowerloft.com.au
• phone number : 0452 918 064
• Street address: 4/83 Kinross Hill Rd, Barrowdale
Nice to have
• Images such as in the attached files.

```html
<!DOCTYPE html>
<html lang="en">
<head>
<meta charset="utf-8">
<title>Barrowdale Power Loft – Chronic Pain Flyer</title>
<link href="https://fonts.googleapis.com/css2?family=Barlow+Condensed:wght@500;600;700&family=Barlow+Semi+Condensed:wght@400;500&display=swap" rel="stylesheet">
<style>
  :root{
    --red:#e02a2a;
    --red-deep:#c81f24;
    --tag-red:#b81c22;
    --charcoal:#3a3a3c;
    --silver:#9a9a9c;
    --white:#ffffff;
    --ink:#3b3b3d;
    --bg:#ecebe8;
  }
  *{margin:0;padding:0;box-sizing:border-box}
  html,body{width:1200px;height:1168px;overflow:hidden;background:var(--bg)}
  body{font-family:"Barlow Condensed",sans-serif;position:relative}
  .flyer{position:absolute;top:64px;width:490px;height:1038px;overflow:hidden;
    background:var(--white);box-shadow:0 6px 18px rgba(0,0,0,.18)}
  .flyer--front{left:82px}
  .flyer--back{left:627px}
  .flyer__art{position:absolute;inset:0;width:490px;height:1038px}
  .brand{position:absolute;font-weight:700;color:var(--ink);text-transform:uppercase;
    text-align:center;line-height:1;letter-spacing:1px;white-space:nowrap}
  .flyer--front .brand{left:48px;top:68px;width:236px;font-size:34px}
  .flyer--back .brand{left:52px;top:52px;width:198px;font-size:29px}
  .headline{position:absolute;color:var(--white);font-weight:700;line-height:1;
    white-space:nowrap;text-shadow:0 2px 3px rgba(0,0,0,.25)}
  .headline__small,.headline__big{display:block}
  .flyer--front .headline{left:0;width:490px;top:262px;text-align:center}
  .flyer--front .headline__small{font-size:52px;font-weight:600;letter-spacing:.5px}
  .flyer--front .headline__big{font-size:82px;letter-spacing:2px;margin-top:-4px}
  .flyer--back .headline{left:70px;top:194px;width:350px;text-align:center}
  .flyer--back .headline__small{font-size:54px;font-weight:600;letter-spacing:.5px}
  .flyer--back .headline__big{font-size:84px;letter-spacing:2px;margin-top:-6px}
  .tagline{position:absolute;left:72px;top:328px;width:341px;height:31px;white-space:nowrap;
    background:var(--tag-red);color:var(--white);font-weight:600;font-size:25px;
    text-align:center;line-height:31px}
  .copy{position:absolute;left:72px;width:346px;color:var(--white);
    font-family:"Barlow Semi Condensed",sans-serif;font-weight:400;
    font-size:18px;line-height:22.7px;text-align:justify;text-align-last:left}
  .copy--intro{top:372px}
  .copy--studio{top:786px}
  .divider{position:absolute;left:154px;top:910px;width:180px;height:2px;background:var(--white)}
  .contact{position:absolute;left:0;width:490px;text-align:center;color:var(--white);white-space:nowrap}
  .flyer--front .contact{top:924px}
  .flyer--back .contact{top:924px}
  .contact__phone{font-size:28px;font-weight:700;line-height:30px}
  .contact__line{font-family:"Barlow Semi Condensed",sans-serif;font-size:22px;font-weight:400;line-height:26px}
</style>
</head>
<body>

<section class="flyer flyer--front">
  <svg class="flyer__art" viewBox="0 0 490 1038">
    <defs>
      <linearGradient id="redFront" x1="0" y1="0" x2="0" y2="1">
        <stop offset="0" stop-color="#e62e2b"/><stop offset="1" stop-color="#c81f24"/>
      </linearGradient>
      <linearGradient id="silverFront" x1="0" y1="0" x2="1" y2="0">
        <stop offset="0" stop-color="#5e5e60"/><stop offset=".5" stop-color="#d8d8da"/><stop offset="1" stop-color="#8c8c8e"/>
      </linearGradient>
      <linearGradient id="gymFront" x1="0" y1="0" x2="1" y2="1">
        <stop offset="0" stop-color="#e9e4dc"/><stop offset=".55" stop-color="#b9a99a"/><stop offset="1" stop-color="#4f6f92"/>
      </linearGradient>
      <radialGradient id="painSpot" cx=".5" cy=".45" r=".6">
        <stop offset="0" stop-color="#e88a8a"/><stop offset=".45" stop-color="#b8b8b8"/><stop offset="1" stop-color="#8a8a8a"/>
      </radialGradient>
    </defs>
    <path d="M0,194 C150,150 330,112 490,30 L490,62 C330,142 150,182 0,206 Z" fill="url(#silverFront)"/>
    <path d="M0,206 C150,186 330,152 490,98 L490,420 C350,458 180,468 0,464 Z" fill="url(#redFront)"/>
    <path d="M0,472 C180,476 350,468 490,430 L490,860 L0,860 Z" fill="url(#gymFront)" role="img" aria-label="Photo: coach guiding a client on a treadmill in the studio"/>
    <path d="M0,826 C200,794 380,808 490,836 L490,848 C380,822 200,808 0,840 Z" fill="url(#silverFront)"/>
    <path d="M0,840 C200,808 380,822 490,848 L490,1038 L0,1038 Z" fill="var(--charcoal)"/>
    <circle cx="70" cy="830" r="70" fill="url(#painSpot)" stroke="#fff" stroke-width="5" role="img" aria-label="Photo: shoulder pain highlighted in red"/>
    <circle cx="198" cy="818" r="66" fill="url(#painSpot)" stroke="#fff" stroke-width="5" role="img" aria-label="Photo: lower back pain highlighted in red"/>
  </svg>
  <div class="brand">Barrowdale<br>Power Loft</div>
  <h1 class="headline"><span class="headline__small">HEALTH THROUGH</span><span class="headline__big">STRENGHT</span></h1>
  <div class="contact">
    <div class="contact__phone">0452 918 064</div>
    <div class="contact__line">barrowdalepowerloft.com.au</div>
    <div class="contact__line">4/83 Kinross Hill Rd, Barrowdale</div>
  </div>
</section>

<section class="flyer flyer--back">
  <svg class="flyer__art" viewBox="0 0 490 1038">
    <defs>
      <linearGradient id="redBack" x1="0" y1="0" x2="0" y2="1">
        <stop offset="0" stop-color="#e62e2b"/><stop offset="1" stop-color="#c81f24"/>
      </linearGradient>
      <linearGradient id="silverBack" x1="0" y1="0" x2="1" y2="0">
        <stop offset="0" stop-color="#5e5e60"/><stop offset=".5" stop-color="#d8d8da"/><stop offset="1" stop-color="#8c8c8e"/>
      </linearGradient>
      <radialGradient id="kneeSpot" cx=".38" cy=".45" r=".7">
        <stop offset="0" stop-color="#ee6a6e"/><stop offset=".25" stop-color="#c9c9c9"/><stop offset="1" stop-color="#f2f2f2"/>
      </radialGradient>
    </defs>
    <path d="M0,156 C180,150 360,112 490,4 L490,40 C360,132 180,164 0,170 Z" fill="url(#silverBack)"/>
    <path d="M0,170 C180,165 360,140 490,56 L490,484 C280,496 120,590 0,700 Z" fill="url(#redBack)"/>
    <path d="M0,700 C120,590 280,496 490,484 L490,498 C280,510 120,604 0,716 Z" fill="url(#silverBack)"/>
    <path d="M0,722 C120,612 280,516 490,504 L490,720 C320,730 150,760 0,790 Z" fill="url(#kneeSpot)" role="img" aria-label="Photo: hands holding a painful knee highlighted in red"/>
    <path d="M0,790 C150,760 320,730 490,720 L490,736 C320,746 150,776 0,806 Z" fill="url(#silverBack)"/>
    <path d="M0,806 C150,776 320,746 490,736 L490,1038 L0,1038 Z" fill="var(--charcoal)"/>
  </svg>
  <div class="brand">Barrowdale<br>Power Loft</div>
  <h2 class="headline"><span class="headline__small">HEALTH THROUGH</span><span class="headline__big">STRENGHT</span></h2>
  <div class="tagline">YOU DON’T HAVE TO LIVE IN PAIN.</div>
  <p class="copy copy--intro">Strenght training has been shown to improve many chronic pain conditions and is now being routinely recommended by medical and health professionals.</p>
  <p class="copy copy--studio">Our private studio provides high quality strenght training by expert strenght coaches. We’ve helped countless people improve or eliminate chronic pain, contact us today and find out how we can help you.</p>
  <div class="divider"></div>
  <div class="contact">
    <div class="contact__phone">0452 918 064</div>
    <div class="contact__line">barrowdalepowerloft.com.au</div>
    <div class="contact__line">4/83 Kinross Hill Rd, Barrowdale</div>
  </div>
</section>

</body>
</html>
```